Flyer for spiritual retreat (yoga, meditation, reiki, raw food)

I would like a flyer to promote my upcoming retreat and a matching Facebook banner.

The name of the retreat is "Wavecrest Of Calm" and the tagline is "retreat into you"

The activities in the retreat include daily meditation, ecstatic dance, spiritual development workshops on intuition, energy healing etc and a reiki session is included.

I would like a flyer designed to promote this, something that is editable as I will be running this multiple times and will need to adjust the flyer to add the dates etc each time.

edit: add that here will be fully catered raw food and juices, and that the retreat price includes all accomodation, meals and workshops.

Please contact me if you need further info. Please also visit my website www.marithovland.com and www.facebook.com/tolvanahaven to see my current events and promotions.

Thank you,

Marit

Reason: Hi all, thank you all for your submissions. Apologies as I am traveling and do not have much access to internet and will review your submissions and provide feedback as soon as possible. Kind regards, Marit.

Target Market(s)

People who like meditation, yoga, fans of rowan mabry and jasper vinek, those interested in personal and spiritual development.

Industry/Entity Type

Health And Wellness

Requirements
Must have
• Please put the included reiki session as as added bonus. Something like "BONUS 30 minute reiki healing session" in a little star/banner/something that stands out.
• Please emphasise the "light" part of Wavecrest as I am going for a play on words between in the light and enlightenment.
• Please include placeholder text for place, location, time
• Placeholder for price
• My name (see attached file - can change colour to suit) and website (www.marithovland.com)
Nice to have
• I prefer rounded designs, curves rather than block designs.
Should not have
• Tolvana Haven logo

```html
<!DOCTYPE html>
<html lang="en">
<head>
<meta charset="utf-8">
<title>Wavecrest Of Calm – Retreat Banners</title>
<link rel="stylesheet" href="https://fonts.googleapis.com/css2?family=Federo&family=Allura&family=Itim&display=swap">
<style>
  :root {
    --peach-light: #fbd3c1;
    --peach: #f7bda7;
    --peach-deep: #efa68d;
    --coral: #e4805f;
    --coral-dark: #d76a4b;
    --card-pale: #fde8df;
    --cream: #fdf3ee;
    --brown: #7a3a2c;
    --signature: #8a5446;
    --white: #ffffff;
  }
  html, body {
    margin: 0;
    padding: 0;
    width: 1200px;
    height: 988px;
    overflow: hidden;
    background: var(--white);
  }
  .canvas {
    position: relative;
    width: 1200px;
    height: 988px;
  }
  .banner {
    position: absolute;
    left: 0;
    width: 1200px;
    height: 444px;
    display: block;
  }
  .banner--plain { top: 35px; }
  .banner--sparkle { top: 510px; }

  .band-label {
    font-family: "Itim", sans-serif;
    font-size: 15px;
    fill: var(--white);
    letter-spacing: 0.3px;
  }
  .card-text {
    font-family: "Itim", sans-serif;
    font-size: 10.5px;
    fill: var(--white);
  }
  .card-text--bold { font-weight: 700; font-size: 11.5px; }
  .price-text {
    font-family: "Itim", sans-serif;
    font-size: 10px;
    fill: var(--coral-dark);
  }
  .price-text--bold { font-size: 11.5px; font-weight: 700; }
  .title {
    font-family: "Federo", sans-serif;
    font-size: 40px;
    fill: var(--brown);
  }
  .title-highlight { fill: var(--coral); }
  .tagline {
    font-family: "Allura", cursive;
    font-size: 26px;
    fill: var(--coral);
  }
  .host-name {
    font-family: "Allura", cursive;
    font-size: 32px;
    fill: var(--signature);
  }
  .website {
    font-family: "Itim", sans-serif;
    font-size: 12.5px;
    font-weight: 700;
    fill: var(--brown);
  }
</style>
</head>
<body>
<main class="canvas">

  <!-- Banner one: plain peach -->
  <svg class="banner banner--plain" viewBox="0 0 851 315" xmlns="http://www.w3.org/2000/svg">
    <defs>
      <linearGradient id="bg-plain" x1="0" y1="0" x2="0" y2="1">
        <stop offset="0" stop-color="var(--peach-light)"/>
        <stop offset="0.55" stop-color="#fac9b5"/>
        <stop offset="1" stop-color="var(--peach)"/>
      </linearGradient>
      <radialGradient id="eye-glow" cx="0.5" cy="0.5" r="0.6">
        <stop offset="0" stop-color="#fefaf8"/>
        <stop offset="0.7" stop-color="var(--cream)"/>
        <stop offset="1" stop-color="#f8dccf"/>
      </radialGradient>
      <radialGradient id="lotus-tone" cx="0.5" cy="0.7" r="0.6">
        <stop offset="0" stop-color="#eeaa95" stop-opacity="0.75"/>
        <stop offset="1" stop-color="#f8c8b3" stop-opacity="0.2"/>
      </radialGradient>
      <radialGradient id="knot-tone" cx="0.5" cy="0.5" r="0.5">
        <stop offset="0" stop-color="var(--coral)" stop-opacity="0.8"/>
        <stop offset="1" stop-color="var(--coral)" stop-opacity="0.15"/>
      </radialGradient>
      <radialGradient id="bokeh-dot" cx="0.5" cy="0.5" r="0.5">
        <stop offset="0" stop-color="#fff" stop-opacity="0.7"/>
        <stop offset="1" stop-color="#fff" stop-opacity="0"/>
      </radialGradient>
      <path id="label-track" d="M0,192 C100,190 170,200 215,214 C290,239 330,287 425,289 C520,291 565,245 625,218 C700,186 770,168 851,155"/>
    </defs>

    <rect width="851" height="315" fill="url(#bg-plain)"/>

    <g id="banner-artwork">
      <ellipse class="lotus" role="img" aria-label="Soft lotus flower decoration behind the title" cx="425" cy="110" rx="210" ry="110" fill="url(#lotus-tone)"/>

      <path class="band band--thin" d="M0,160 C110,158 160,200 205,195 C275,180 330,108 425,106 C520,104 570,180 640,192 C700,200 780,170 851,150" fill="none" stroke="var(--coral)" stroke-width="9"/>

      <path class="eye-panel" d="M205,198 C275,182 330,113 425,111 C520,109 570,178 628,196 C565,236 520,283 425,283 C330,283 285,234 205,198 Z" fill="url(#eye-glow)"/>

      <path class="band band--labels" d="M0,192 C100,190 170,200 215,214 C290,239 330,287 425,289 C520,291 565,245 625,218 C700,186 770,168 851,155" fill="none" stroke="var(--coral)" stroke-width="22"/>

      <text class="band-label" dy="5"><textPath href="#label-track" startOffset="2.5%">daily meditation</textPath></text>
      <text class="band-label" dy="5"><textPath href="#label-track" startOffset="25%">energy healing</textPath></text>
      <text class="band-label" dy="5"><textPath href="#label-track" startOffset="42%">ecstatic dance</textPath></text>
      <text class="band-label" dy="5"><textPath href="#label-track" startOffset="59%">spiritual development</textPath></text>
      <text class="band-label" dy="5"><textPath href="#label-track" startOffset="80%">workshops on intuition</textPath></text>

      <ellipse class="knot-ornament" role="img" aria-label="Small heart knot ornament" cx="425" cy="142" rx="15" ry="18" fill="url(#knot-tone)"/>

      <text class="title" x="425" y="203" text-anchor="middle">Wave<tspan class="title-highlight">crest</tspan> Of Calm</text>
      <text class="tagline" x="455" y="232" text-anchor="middle">retreat into you</text>

      <g class="card card--dates" transform="translate(105 128) rotate(15)">
        <rect x="-92" y="-50" width="184" height="100" rx="12" fill="var(--coral)" stroke="var(--card-pale)" stroke-width="1.5"/>
        <text class="card-text card-text--bold" x="0" y="-28" text-anchor="middle">20.-22.1.2017</text>
        <text class="card-text" x="0" y="-6" text-anchor="middle">@ Tolvana Haven</text>
        <text class="card-text" x="0" y="10" text-anchor="middle">U3/12 Harbour Lane</text>
        <text class="card-text" x="0" y="26" text-anchor="middle">Coralby, Westhaven</text>
      </g>

      <g class="card card--bonus" transform="translate(697 120) rotate(-3)">
        <rect x="-92" y="-30" width="184" height="60" rx="11" fill="var(--coral)" stroke="var(--card-pale)" stroke-width="1.5"/>
        <text class="card-text card-text--bold" x="0" y="-11" text-anchor="middle">BONUS</text>
        <text class="card-text" x="0" y="7" text-anchor="middle">30 minute reiki session</text>
        <text class="card-text" x="0" y="21" text-anchor="middle">included</text>
      </g>

      <g class="card card--price" transform="translate(752 255) rotate(-10)">
        <rect x="-95" y="-40" width="190" height="80" rx="12" fill="var(--card-pale)" stroke="var(--peach-deep)" stroke-width="1.5"/>
        <text class="price-text price-text--bold" x="0" y="-18" text-anchor="middle">XXX A$</text>
        <text class="price-text" x="0" y="2" text-anchor="middle">includes all accomodation,</text>
        <text class="price-text" x="0" y="16" text-anchor="middle">workshops and meals with fully</text>
        <text class="price-text" x="0" y="30" text-anchor="middle">catered raw food and juices.</text>
      </g>

      <text class="host-name" x="12" y="280">Marit Hovland</text>
      <text class="website" x="15" y="303">www.marithovland.com</text>
    </g>
  </svg>

  <!-- Banner two: sparkle background -->
  <svg class="banner banner--sparkle" viewBox="0 0 851 315" xmlns="http://www.w3.org/2000/svg">
    <defs>
      <linearGradient id="bg-sparkle" x1="0" y1="0" x2="0" y2="1">
        <stop offset="0" stop-color="#f9cdbb"/>
        <stop offset="0.55" stop-color="#f2b8a3"/>
        <stop offset="1" stop-color="#eaa38c"/>
      </linearGradient>
    </defs>
    <rect width="851" height="315" fill="url(#bg-sparkle)"/>
    <g class="bokeh">
      <circle cx="40" cy="30" r="10" fill="url(#bokeh-dot)"/>
      <circle cx="150" cy="60" r="7" fill="url(#bokeh-dot)"/>
      <circle cx="260" cy="25" r="12" fill="url(#bokeh-dot)"/>
      <circle cx="600" cy="40" r="9" fill="url(#bokeh-dot)"/>
      <circle cx="720" cy="20" r="14" fill="url(#bokeh-dot)"/>
      <circle cx="820" cy="70" r="8" fill="url(#bokeh-dot)"/>
      <circle cx="90" cy="230" r="9" fill="url(#bokeh-dot)"/>
      <circle cx="190" cy="285" r="12" fill="url(#bokeh-dot)"/>
      <circle cx="300" cy="300" r="7" fill="url(#bokeh-dot)"/>
      <circle cx="560" cy="295" r="10" fill="url(#bokeh-dot)"/>
      <circle cx="640" cy="280" r="6" fill="url(#bokeh-dot)"/>
      <circle cx="830" cy="300" r="11" fill="url(#bokeh-dot)"/>
      <circle cx="500" cy="70" r="6" fill="url(#bokeh-dot)"/>
      <circle cx="360" cy="60" r="5" fill="url(#bokeh-dot)"/>
    </g>
    <use href="#banner-artwork"/>
  </svg>

</main>
</body>
</html>
```